Artificial intelligence, machine learning, and automation company needs a sexy business card design

We need a sleek and sexy business card design for an AI consulting company based in Philadelphia PA. We provide custom machine learning and automation solutions for companies of all shapes and sizes. The primary industries that we serve are pharmaceuticals, engineering, healthcare, and computer software. We would like the designs to be a black business card that uses green as a sleek accent color. The final design should communicate intelligence, cutting edge new-tech, and optimization.

Target Market(s)

C-level and VP level executives of multi-million annual companies. Mostly in Pharma, Healthcare, Real Estate, Retail, and Engineering

Industry/Entity Type

Computer Software

Contact Information for Business Card

Name: Jed Harlow
Title: CEO
Cell: 484 562 0937
Email: JedH@quillorbit.example
Website: www.QuillOrbit.example

Font styles to use
Sans Serif

Colors

Designer to choose colors to be used in the design.

Requirements
Must have
• 1) Attached Quillon Logo (either with colors or not/embossed)
• 2) "Artificial Intelligence" "Automation" and "Machine Learning"
• 3) "Quillon Laboratories" or "Quillon Labs" or "Quillon"
• 4) Sexy AF.
Nice to have
• Black card / dark card color, "Quillon Green" accent colors (in attached .ai file), Embossment of logo/name/etc, thick card stock, colored borders (on card sides, not front/back faces)
Should not have
• Should not be bland, or unsexy.

```html
<!DOCTYPE html>
<html lang="en">
<head>
<meta charset="utf-8">
<title>Quillon Laboratories – Business Card</title>
<link rel="stylesheet" href="https://fonts.googleapis.com/css2?family=Montserrat:wght@400;600&family=Open+Sans:wght@400&display=swap">
<style>
  :root {
    --backdrop: #5e4330;
    --card-front: #2b2b2b;
    --card-back: #232323;
    --tile-faint: #393939;
    --quillon-green: #4fc9ad;
    --text-light: #f2f2f2;
    --rule: #cfcfcf;
  }
  html, body {
    margin: 0;
    padding: 0;
    width: 1200px;
    height: 1000px;
    overflow: hidden;
    background: var(--backdrop);
  }
  .canvas {
    position: relative;
    width: 1200px;
    height: 1000px;
  }
  .card {
    position: absolute;
    left: 267px;
    width: 665px;
    height: 397px;
    box-shadow: 0 6px 18px rgba(0,0,0,0.45);
    overflow: hidden;
  }
  .card-front {
    top: 74px;
    background: var(--card-front);
  }
  .tile-grid {
    position: absolute;
    left: 7px;
    top: 5px;
    display: grid;
    grid-template-columns: repeat(8, 63px);
    grid-auto-rows: 63px;
    column-gap: 21.5px;
    row-gap: 18px;
  }
  .tile {
    border: 3px solid var(--tile-faint);
    box-sizing: border-box;
  }
  .tile-accent {
    border-color: var(--quillon-green);
  }
  .card-back {
    top: 533px;
    background: var(--card-back);
  }
  .brand {
    position: absolute;
    left: 147px;
    top: 86px;
    display: flex;
    align-items: center;
    gap: 16px;
  }
  .brand-square {
    width: 59px;
    height: 59px;
    border: 3px solid var(--quillon-green);
    box-sizing: border-box;
  }
  .brand-name {
    font-family: "Montserrat", sans-serif;
    font-weight: 400;
    color: var(--text-light);
    line-height: 1;
  }
  .brand-name .line-main {
    display: block;
    font-size: 31px;
    letter-spacing: 4.5px;
  }
  .brand-name .line-sub {
    display: block;
    margin-top: 9px;
    font-size: 16.5px;
    letter-spacing: 3.4px;
  }
  .person {
    position: absolute;
    left: 146px;
    top: 199px;
  }
  .person-name {
    margin: 0;
    font-family: "Montserrat", sans-serif;
    font-weight: 600;
    font-size: 24px;
    color: var(--quillon-green);
    line-height: 1.1;
  }
  .person-title {
    margin: 3px 0 0;
    font-family: "Open Sans", sans-serif;
    font-size: 15px;
    color: var(--text-light);
  }
  .divider {
    position: absolute;
    left: 146px;
    top: 260px;
    width: 324px;
    height: 1px;
    background: var(--rule);
  }
  .contact {
    position: absolute;
    left: 146px;
    top: 273px;
    font-family: "Open Sans", sans-serif;
    font-size: 15.5px;
    color: var(--text-light);
    line-height: 23px;
  }
  .contact-row {
    display: flex;
    align-items: center;
    gap: 5px;
  }
  .contact-row .gap { width: 3px; }
  .contact svg {
    width: 13px;
    height: 13px;
    fill: none;
    stroke: var(--quillon-green);
    stroke-width: 1.6;
  }
</style>
</head>
<body>
<main class="canvas">
  <section class="card card-front" aria-label="Card front">
    <div class="tile-grid">
      <div class="tile"></div><div class="tile"></div><div class="tile"></div><div class="tile"></div>
      <div class="tile"></div><div class="tile"></div><div class="tile"></div><div class="tile"></div>

      <div class="tile"></div><div class="tile"></div><div class="tile tile-accent"></div><div class="tile"></div>
      <div class="tile"></div><div class="tile"></div><div class="tile"></div><div class="tile"></div>

      <div class="tile"></div><div class="tile"></div><div class="tile"></div><div class="tile"></div>
      <div class="tile"></div><div class="tile"></div><div class="tile"></div><div class="tile"></div>

      <div class="tile"></div><div class="tile"></div><div class="tile"></div><div class="tile"></div>
      <div class="tile"></div><div class="tile"></div><div class="tile"></div><div class="tile"></div>

      <div class="tile"></div><div class="tile"></div><div class="tile"></div><div class="tile"></div>
      <div class="tile"></div><div class="tile"></div><div class="tile"></div><div class="tile"></div>
    </div>
  </section>

  <section class="card card-back">
    <div class="brand">
      <div class="brand-square"></div>
      <div class="brand-name">
        <span class="line-main">QUILLON</span>
        <span class="line-sub">LABORATORIES</span>
      </div>
    </div>

    <div class="person">
      <h1 class="person-name">JED HARLOW</h1>
      <p class="person-title">CEO</p>
    </div>

    <div class="divider"></div>

    <div class="contact">
      <div class="contact-row">
        <svg viewBox="0 0 16 16" aria-hidden="true"><path d="M3 1.5l3 3-1.5 2a8 8 0 0 0 5 5l2-1.5 3 3-2 2C6 14.5 1.5 10 1 3.5z"/></svg>
        <span>484 562 0937</span>
        <span class="gap"></span>
        <svg viewBox="0 0 16 16" aria-hidden="true"><rect x="1" y="3" width="14" height="10"/><path d="M1 3l7 6 7-6"/></svg>
        <span>JedH@quillorbit.example</span>
      </div>
      <div class="contact-row">www.QuillOrbit.example</div>
    </div>
  </section>
</main>
</body>
</html>
```